Liebe Kreativgemeinde,
gesucht wird ein geschmackvolles Corporate Design für den Außenauftritt eines Hamburger Handwerksbetriebs,
dass die Werte „Vertrauen und Verlässlichkeit“, „Wertigkeit“ und erstklassige „Handwerkskunst“ in einem zeitgemäßen Design miteinander verbindet.
Das hanseatische „FliesenHof Krell“ hat es sich zur Aufgabe gemacht, Kunden im oberen Preissegment mit Beratung, Verkauf und Installation von erstklassigen Bodenbelegen zur Seite zu stehen.
Ob für Wohnungs- oder Ladenbau: alte Böden, Treppen und Betonflächen werden von „FliesenHof Krell“ professionell abgeschliffen und aufbereitet – hochwertige Designbodenbeläge, Holzdielen und Parkett werden fachgerecht verlegt.
„FliesenHof Krell“ spricht dabei eine Zielgruppe an, deren Fokus nicht auf „möglichst schnell und möglichst günstig“ liegt, sondern die der deutschen Handwerkstugend und ihrem hohen Qualitätsstandard eine bewusste Wertschätzung entgegen bringt.
Wir sind gespannt auf Eure Ideen!
Euer „FliesenHof Krell“

```html
<!DOCTYPE html>
<html lang="en">
<head>
<meta charset="utf-8">
<title>FliesenHof Krell – Stationery Concept</title>
<link href="https://fonts.googleapis.com/css2?family=Carlito:wght@400;700&family=Libre+Baskerville:wght@700&family=Source+Sans+3:wght@400&family=Arimo&display=swap" rel="stylesheet">
<style>
  :root {
    --board: #a6a6a6;
    --paper: #ffffff;
    --brand: #7b3f0c;
    --ink: #1c1c1c;
    --label: #ffffff;
    --mark-light: #e3e3e3;
    --sign-tone: #d9d9d9;
  }
  * { margin: 0; padding: 0; box-sizing: border-box; }
  html, body { width: 1200px; height: 1200px; overflow: hidden; }
  body {
    position: relative;
    background: var(--board);
    font-family: "Carlito", "Calibri", sans-serif;
    color: var(--ink);
  }
  .brand-name {
    font-family: "Libre Baskerville", serif;
    font-weight: 700;
    line-height: 0.95;
    letter-spacing: 0.02em;
    text-transform: uppercase;
  }
  .brand-square { display: inline-block; background: var(--brand); }

  /* Letterhead */
  .letterhead {
    position: absolute; left: 102px; top: 59px; width: 662px; height: 1011px;
    background: var(--paper);
    box-shadow: 3px 4px 8px rgba(0,0,0,0.35);
    font-size: 11px; line-height: 15.6px;
  }
  .letterhead .brand {
    position: absolute; left: 50px; top: 60px;
    display: flex; align-items: center; gap: 10px;
  }
  .letterhead .brand-square { width: 34px; height: 34px; }
  .letterhead .brand-name { font-size: 16px; color: var(--brand); }
  .contact { position: absolute; left: 504px; top: 56px; }
  .contact .gap { height: 15.6px; }
  .contact b { color: var(--brand); }
  .date { position: absolute; left: 43px; top: 203px; }
  .recipient { position: absolute; left: 43px; top: 234px; }
  .recipient .name { font-weight: 700; margin-bottom: 15.6px; }
  .letter-body { position: absolute; left: 43px; top: 352px; width: 578px; text-align: justify; }
  .letter-body p + p { margin-top: 15.6px; }
  .closing { position: absolute; left: 43px; top: 693px; }
  .signature { position: absolute; left: 39px; top: 721px; width: 170px; height: 50px; background: var(--sign-tone); border-radius: 4px; }
  .signer { position: absolute; left: 100px; top: 756px; }
  .signer .name { font-weight: 700; font-size: 12px; }
  .signer .role { margin-left: 2px; }
  .bank { position: absolute; left: 43px; top: 926px; line-height: 15.2px; }
  .bank b { font-weight: 700; }

  /* Presentation mark */
  .presentation-mark {
    position: absolute; left: 809px; top: 78px;
    display: flex; align-items: center; gap: 22px;
  }
  .presentation-mark .brand-square { width: 64px; height: 64px; background: var(--mark-light); }
  .presentation-mark .brand-name { font-size: 25px; color: var(--mark-light); }

  /* Cards */
  .card {
    position: absolute; left: 817px; width: 302px; height: 172px;
    box-shadow: 3px 4px 8px rgba(0,0,0,0.35);
  }
  .card-front { top: 516px; background: var(--paper); }
  .card-front .brand { position: absolute; left: 22px; top: 70px; display: flex; align-items: center; gap: 6px; }
  .card-front .brand-square { width: 18px; height: 18px; }
  .card-front .brand-name { font-size: 9px; color: var(--brand); }
  .card-front .contact { left: 178px; top: 46px; font-size: 8.2px; line-height: 11px; }
  .card-front .contact .gap { height: 11px; }
  .card-back { top: 751px; background: var(--brand); display: flex; justify-content: center; align-items: center; gap: 7px; }
  .card-back .brand-square { width: 20px; height: 20px; background: var(--paper); }
  .card-back .brand-name { font-size: 10px; color: var(--paper); }

  .label {
    position: absolute; font-family: "Source Sans 3", sans-serif;
    font-size: 17px; color: var(--label);
  }
  .note {
    position: absolute; left: 29px; top: 1121px;
    font-family: "Arimo", Arial, sans-serif; font-size: 13px; line-height: 17px; color: var(--label);
  }
</style>
</head>
<body>

<section class="letterhead">
  <div class="brand"><span class="brand-square"></span><span class="brand-name">FliesenHof<br>Krell</span></div>
  <address class="contact" style="font-style:normal">
    Company Name<br>Lindenkai 12<br>The Netherlands
    <div class="gap"></div>
    <b>P:</b> +31 6 55501234<br><b>C:</b> +31 6 55501234<br><b>E:</b> post@musterbuero.com
  </address>
  <div class="date">Date</div>
  <div class="recipient">
    <div class="name">Recipient Name</div>
    Company Name<br>Street Address<br>City, State, Zip
  </div>
  <div class="letter-body">
    <p>Lorem ipsum dolor sit amet, consectetur adipiscing elit. Vestibulum congue vel orci non aliquet. Sed tristique elit nulla, in aliquet massa consequat id. Mauris gravida eget ante et cursus. Cras faucibus ac urna in fringilla. Morbi sed feugiat felis, et maximus lorem. Integer dictum sed odio non auctor. Fusce interdum nisl non nulla blandit, id commodo orci laoreet. Donec et ligula non quam malesuada congue non nec mauris.</p>
    <p>Sed vel orci id diam dignissim sagittis. Maecenas molestie pulvinar sapien, quis iaculis nisl ultricies hendrerit. Donec imperdiet arcu tincidunt, laoreet eros interdum, scelerisque justo. Sed sit amet massa ac tortor porta finibus. Phasellus sed est aliquet, laoreet lacus nec, consectetur sem. Sed et magna felis. Phasellus lobortis orci quis cursus imperdiet. Nullam id arcu sollicitudin, efficitur enim quis, venenatis tortor. Donec fermentum sapien nulla, in fringilla odio sollicitudin et. Ut libero mi, lacinia sit amet sem sed, condimentum laoreet nisl. Sed dapibus enim ut tellus hendrerit, sit amet vestibulum mi molestie. Phasellus tincidunt nisl id neque convallis ullamcorper. Vivamus lacinia viverra tellus tristique elementum. Aenean nisi augue, luctus vel elementum nec, tristique nec libero.</p>
    <p>Mauris quis turpis est. Morbi a odio ullamcorper, lacinia lorem eu, varius justo. Phasellus semper fermentum dignissim. Morbi fermentum odio nec sem feugiat blandit. Suspendisse faucibus massa non ex fringilla congue. Aliquam hendrerit nec elit id iaculis. Sed imperdiet metus eget odio scelerisque posuere. Proin finibus interdum semper. Morbi sodales facilisis justo vitae maximus. Aliquam facilisis urna in velit condimentum maximus. Etiam vitae justo ligula. Nulla facilisis faucibus diam.</p>
  </div>
  <div class="closing">Sincerely,</div>
  <div class="signature" role="img" aria-label="Handwritten signature"></div>
  <div class="signer"><div class="name">Jan Meier</div><div class="role">CEO</div></div>
  <div class="bank">
    <b>BANKVERBINDUNG:</b> HB BANK &amp; TREUHAND<br>
    <b>STEUERNUMMER:</b> 000000000000<br>
    <b>FAX NO.:</b> 000000000000<br>
    <b>WEBSITE:</b> WWW.MUSTERBUERO.COM
  </div>
</section>
<div class="label" style="left:100px; top:1088px;">Letterhead</div>

<div class="presentation-mark"><span class="brand-square"></span><span class="brand-name">FliesenHof<br>Krell</span></div>
<div class="label" style="left:814px; top:211px;">Stationary concept</div>

<section class="card card-front">
  <div class="brand"><span class="brand-square"></span><span class="brand-name">FliesenHof<br>Krell</span></div>
  <address class="contact" style="font-style:normal">
    Company Name<br>Lindenkai 12<br>The Netherlands
    <div class="gap"></div>
    <b>P:</b> +31 6 55501234<br><b>C:</b> +31 6 55501234<br><b>E:</b> post@musterbuero.com
  </address>
</section>
<div class="label" style="left:815px; top:700px;">Front card</div>

<section class="card card-back">
  <span class="brand-square"></span><span class="brand-name">FliesenHof<br>Krell</span>
</section>
<div class="label" style="left:815px; top:937px;">Back card</div>

<div class="note">2017 FLIESENHOF KRELL LOGO.<br>LOGO IS PRESENTED AS DRAFT AND CAN BE MODIFIED UPON REQUEST.</div>

</body>
</html>
```